Energy Company 8-page Brochure

We are in need of a redesign of our 8-page brochure. Attached is the initial design that does not represent us very well. We are looking for CLEAN/CORPORATE look with a little bit of flair (graphs/charts if applicable).

I prefer white background and our company colors (blue/green) to be the accent colors. Feel free to add additional accent colors to highlight certain areas.

We are in the energy field (not just solar), so please consider the types of images that you will use. Are headquarters is located in Chicago, IL so a great looking picture of the skyline or something similar would work for the front and back cover.

We have additional marketing collateral that we will want to be uniformed once we have the right design.

Good luck, and we look forward to receiving some great designs!

Best Regards,
Rob

Target Market(s)

Small to large businesses (B2B).

Industry/Entity Type

It Company

Colors
ffffff
9bcb3c
0255a3

Requirements
Must have
• Clean design, company colors, specified content and editable files.
Nice to have
• Graphs, charts, highlighted areas where necessary.
Should not have
• Clutter! Please utilized page space appropriately. There is a lot of content, so you need to consider graphics and image placement.

```html
<!DOCTYPE html>
<html lang="en">
<head>
<meta charset="utf-8">
<title>Everything Energy – Brochure Cover</title>
<link href="https://fonts.googleapis.com/css2?family=Open+Sans:wght@300;400;700&display=swap" rel="stylesheet">
<style>
  :root {
    --brand-blue: #0a5a9c;
    --brand-green: #58a333;
    --paper: #ffffff;
    --stage: #e6e6e6;
    --ink-light: #ffffff;
  }
  * { box-sizing: border-box; margin: 0; padding: 0; }
  html, body {
    width: 993px; height: 1200px; overflow: hidden;
    background: var(--stage);
    font-family: "Open Sans", Arial, sans-serif;
  }
  .cover {
    position: relative;
    width: 993px; height: 1200px;
    background: var(--brand-blue);
    overflow: hidden;
  }
  .masthead {
    position: absolute; top: 0; left: 0; right: 0;
    height: 182px;
    background: var(--paper);
    display: flex; align-items: center;
    padding-left: 80px; gap: 48px;
  }
  .brand {
    display: flex; align-items: center; gap: 14px;
    font-weight: 400; font-size: 27px; line-height: 1.05;
  }
  .brand--primary { color: var(--brand-blue); }
  .brand--partner { color: var(--brand-green); }
  .brand__dot {
    width: 62px; height: 62px; border-radius: 50%;
    background: var(--brand-blue);
  }
  .headline {
    position: absolute; left: 72px; top: 258px;
    color: var(--ink-light);
    font-size: 116px; line-height: 1.08; letter-spacing: -1px;
  }
  .headline__light { display: block; font-weight: 300; }
  .headline__bold { display: block; font-weight: 700; }
  .benefits {
    position: absolute; left: 80px; top: 550px;
    display: grid;
    grid-template-columns: 250px 250px;
    row-gap: 34px;
    list-style: none;
  }
  .benefit {
    display: flex; align-items: center; gap: 16px;
    color: var(--ink-light);
    font-size: 19px; font-weight: 300; line-height: 1.25;
  }
  .benefit b { font-weight: 700; }
  .benefit__icon {
    flex: none; width: 52px; height: 52px; border-radius: 50%;
    background: var(--paper);
    display: flex; align-items: center; justify-content: center;
  }
  .benefit--wide { grid-column: 1; }
  .emblem-area {
    position: absolute; left: 430px; top: 700px;
    width: 600px; height: 520px;
    background: radial-gradient(circle at 55% 60%, rgba(255,255,255,0.55) 0%, rgba(255,255,255,0.22) 45%, rgba(255,255,255,0) 72%);
  }
</style>
</head>
<body>
<main class="cover">
  <header class="masthead">
    <div class="brand brand--primary">
      <span class="brand__dot"></span>
      <span>Brightline<br>Power</span>
    </div>
    <div class="brand brand--partner">
      <span>Kilowatt<br>Advisors</span>
    </div>
  </header>

  <h1 class="headline">
    <span class="headline__light">Everything</span>
    <span class="headline__bold">Energy</span>
  </h1>

  <ul class="benefits">
    <li class="benefit">
      <span class="benefit__icon">
        <svg width="30" height="30" viewBox="0 0 30 30"><circle cx="15" cy="15" r="12" fill="none" stroke="#0a5a9c" stroke-width="3"/><text x="15" y="21" text-anchor="middle" font-family="Open Sans, sans-serif" font-weight="700" font-size="16" fill="#0a5a9c">$</text></svg>
      </span>
      <span>We <b>manage<br>pricing</b> volatility.</span>
    </li>
    <li class="benefit">
      <span class="benefit__icon">
        <svg width="30" height="30" viewBox="0 0 30 30"><polyline points="4,10 13,19 17,14 26,22" fill="none" stroke="#0a5a9c" stroke-width="2.5"/><polyline points="20,22 26,22 26,16" fill="none" stroke="#0a5a9c" stroke-width="2.5"/></svg>
      </span>
      <span>We <b>mitigate</b> risk.</span>
    </li>
    <li class="benefit">
      <span class="benefit__icon">
        <svg width="30" height="30" viewBox="0 0 30 30"><ellipse cx="15" cy="16" rx="11" ry="8" fill="#0a5a9c"/><rect x="8" y="21" width="3" height="5" fill="#0a5a9c"/><rect x="19" y="21" width="3" height="5" fill="#0a5a9c"/></svg>
      </span>
      <span>We <b>secure</b><br>the lowest cost.</span>
    </li>
    <li class="benefit">
      <span class="benefit__icon">
        <svg width="30" height="30" viewBox="0 0 30 30"><circle cx="15" cy="12" r="7" fill="none" stroke="#0a5a9c" stroke-width="2.5"/><rect x="11" y="20" width="8" height="6" rx="1" fill="#0a5a9c"/></svg>
      </span>
      <span>We <b>lower</b><br>energy usage.</span>
    </li>
    <li class="benefit benefit--wide">
      <span class="benefit__icon">
        <svg width="30" height="30" viewBox="0 0 30 30"><circle cx="15" cy="11" r="5" fill="#0a5a9c"/><rect x="6" y="19" width="18" height="8" fill="#0a5a9c"/></svg>
      </span>
      <span>We <b>reflect</b> your<br>energy values.</span>
    </li>
  </ul>

  <div class="emblem-area" role="img" aria-label="Large white atom-style emblem with orbiting rings and circles as cover decoration"></div>
</main>
</body>
</html>
```